Postcard Design Project

Compliance Tools for your Ambulatory Surgery Center
from the leader in ASC Regulatory Education - Peter R. Vandamore, MBA, CASC, CPA and Marlow Ridge Partners, Inc.

Three Tools Available:

1) The Clinic Rulebook Hour with Peter Vandamore
A weekly podcast for Freestanding Ambulatory Surgery Centers with Industry Leader Peter R. Vandamore, MBA, CASC, CPA. Mr. Vandamore is the author of 10 books about the ASC industry and a frequent speaker at industry meetings.
Available on Soundvale, Brisk Shelf, ViewTrove, Wavelet and Castrill or visit the website at www.clinicrulebookhour.example

Books

2) Steering the Outpatient Suite - A Handbook for Facility Proprietors & Oversight Board Directors
This book provides guidance to owners and board members on their responsibilities.

and

3) The Inspection Primer for Day Clinics - A Handbook on Federal Payment Standards & Reviewer Instructions for Outpatient Procedure Facilities
The industry's leading guide to preparing for a Medicare Survey.

I have provided an example of a previous post card advertising only one product - one of the books.

I am hoping to advertise the various products offered by my company (Marlow Ridge Partners) and myself (Peter Vandamore) to assist Ambulatory Surgery Centers in keeping up with the latest regulations and requirements to stay in business.

Please make sure that the post card meets all of the requirements of bulk mail with the post office.

```html
<!DOCTYPE html>
<html lang="en">
<head>
<meta charset="utf-8">
<title>Postcard – Front and Back</title>
<link rel="stylesheet" href="https://fonts.googleapis.com/css2?family=Cinzel:wght@400;700&family=Open+Sans:wght@400;600&family=Roboto+Condensed:wght@400&family=Crimson+Text:ital,wght@0,400;1,700&display=swap">
<style>
  :root{
    --page:#e4e4e4;
    --navy:#163a6b;
    --navy-deep:#13335f;
    --blue:#1f5aa6;
    --blue-mid:#2a63ad;
    --photo-grey:#c9c9cb;
    --white:#ffffff;
    --panel-grey:#dedede;
    --ink:#1a1a1a;
    --accent:#49c6f0;
    --title-yellow:#f2d23a;
    --cover-blue:#1c4e96;
    --cover-violet:#2f3c93;
  }
  *{box-sizing:border-box;margin:0;padding:0}
  html,body{width:1200px;height:1000px;overflow:hidden}
  body{background:var(--page);position:relative;font-family:"Cinzel",serif}

  /* ---------- Front ---------- */
  .card-front{position:absolute;left:73px;top:40px;width:596px;height:432px;background:var(--blue);overflow:hidden}
  .front-header{position:absolute;left:0;top:0;width:100%;height:75px;background:var(--navy);color:var(--white);text-align:center;padding-top:20px;font-size:15px;line-height:18px;letter-spacing:.3px}
  .front-header .author{font-size:13px;font-weight:700;color:#d9e4f5;display:block}
  .front-photo{position:absolute;left:0;top:75px;width:100%;height:227px;background:linear-gradient(90deg,#d6d6d8,#b9babd 50%,#d2d2d4)}
  .book{position:absolute;top:82px;width:136px;height:224px;box-shadow:4px 4px 8px rgba(0,0,0,.35)}
  .book-gov{left:78px;background:var(--cover-blue)}
  .book-survey{left:364px;background:var(--cover-violet)}
  .book .cover-title{position:absolute;left:8px;top:16px;right:6px;font-family:"Crimson Text",serif;font-style:italic;font-weight:700;font-size:12px;line-height:13px}
  .book-gov .cover-title{color:var(--title-yellow)}
  .book-survey .cover-title{color:var(--white);font-style:normal}
  .book .cover-sub{position:absolute;left:8px;right:6px;top:48px;font-family:"Crimson Text",serif;font-size:7.5px;line-height:9px;color:var(--white)}
  .book .cover-photo{position:absolute;left:0;right:0;top:92px;height:90px;background:linear-gradient(#6f8fbf,#3c5f94)}
  .book-survey .cover-photo{left:8px;right:8px;top:96px;height:100px;background:linear-gradient(#9a9a9a,#4a4a4a)}
  .book .cover-author{position:absolute;left:0;right:0;bottom:10px;text-align:center;font-family:"Crimson Text",serif;font-size:8px;color:var(--white)}
  .book-survey .cover-author{bottom:4px;font-size:6.5px}
  .book-blurb{position:absolute;top:310px;width:270px;text-align:center;color:var(--white)}
  .blurb-gov{left:10px}
  .blurb-survey{left:310px}
  .book-blurb h2{font-size:14px;line-height:14px;font-weight:400}
  .book-blurb p{font-size:7px;line-height:8px;margin-top:2px}
  .blurb-gov p.first{margin-top:0}
  .front-footer{position:absolute;left:0;bottom:0;width:100%;height:35px;background:var(--navy-deep);color:var(--white);text-align:center;font-size:14px;line-height:35px;letter-spacing:.3px}

  /* ---------- Back ---------- */
  .card-back{position:absolute;left:540px;top:520px;width:596px;height:433px;background:var(--white);overflow:hidden}
  .back-panel{position:absolute;left:0;top:192px;width:300px;height:241px;background:var(--panel-grey)}
  .stamp-box{position:absolute;left:487px;top:31px;width:78px;height:77px;border:1px solid #555}
  .show-mark{position:absolute;left:130px;top:34px;width:40px;height:40px;border-radius:50%;background:var(--navy)}
  .show-title{position:absolute;left:0;width:300px;top:98px;text-align:center;font-family:"Open Sans",sans-serif;font-size:18px;color:var(--ink)}
  .show-host{position:absolute;left:0;width:300px;top:126px;text-align:center;font-family:"Open Sans",sans-serif;font-size:16px;color:var(--navy-deep)}
  .show-about{position:absolute;left:28px;top:160px;width:243px;height:90px;background:var(--navy);border-radius:8px;color:var(--white);text-align:center;font-size:9px;line-height:11px;padding:7px 10px}
  .show-about .host-name{color:var(--accent);font-weight:700}
  .available{position:absolute;left:0;width:300px;top:268px;text-align:center;font-size:11px;font-weight:700;color:var(--navy-deep)}
  .platforms{position:absolute;left:20px;width:260px;top:287px;display:flex;flex-wrap:wrap;justify-content:center;gap:4px 10px;font-family:"Open Sans",sans-serif;font-size:11px;font-weight:600;color:var(--ink)}
  .visit{position:absolute;left:0;width:300px;top:350px;text-align:center;font-size:10px;font-weight:700;color:var(--navy-deep)}
  .site{position:absolute;left:0;width:300px;top:366px;text-align:center;font-family:"Roboto Condensed",sans-serif;font-size:19px;color:var(--ink)}
</style>
</head>
<body>

<section class="card-front" aria-label="Postcard front">
  <header class="front-header">
    Compliance Tools for Your Ambulatory Surgery Center<br>
    From the Leader in ASC Regulatory Education
    <span class="author">Peter R. Vandamore, MBA, CASC, CPA</span>
  </header>
  <div class="front-photo" role="img" aria-label="Faded greyscale photo of a surgeon in an operating room"></div>

  <div class="book book-gov">
    <div class="cover-title">Steering the Outpatient Suite</div>
    <div class="cover-sub">A Handbook for Facility Proprietors and Oversight Board Directors</div>
    <div class="cover-photo" role="img" aria-label="Photo of surgeons at work"></div>
    <div class="cover-author">Peter R. Vandamore, MBA, CASC</div>
  </div>
  <div class="book book-survey">
    <div class="cover-title">The Inspection Primer for Day Clinics</div>
    <div class="cover-sub">A Handbook on Federal Payment Standards &amp; Reviewer Instructions for Outpatient Procedure Facilities</div>
    <div class="cover-photo" role="img" aria-label="Black and white photo of an operating room"></div>
    <div class="cover-author">Peter R. Vandamore, MBA, CASC</div>
  </div>

  <div class="book-blurb blurb-gov">
    <h2>Steering the<br>Outpatient Suite</h2>
    <p>A Handbook for Facility Proprietors<br>&amp; Oversight Board Directors</p>
    <p>This book provides guidance to owners and<br>board members on their responsibilities.</p>
  </div>
  <div class="book-blurb blurb-survey">
    <h2>The Inspection Primer<br>for Day Clinics</h2>
    <p>A Handbook on Federal Payment Standards &amp;<br>Reviewer Instructions for Outpatient Procedure Facilities</p>
    <p>The industry's leading guide to preparing<br>for a Medicare survey.</p>
  </div>

  <footer class="front-footer">Order Online at&nbsp; www.rulebookpress.example</footer>
</section>

<section class="card-back" aria-label="Postcard back">
  <div class="back-panel"></div>
  <div class="stamp-box" aria-label="Postage area"></div>
  <div class="show-mark"></div>
  <div class="show-title">Clinic Rulebook Hour</div>
  <div class="show-host">with Peter Vandamore</div>
  <div class="show-about">
    A weekly podcast for freestanding ambulatory surgery centers with industry leader
    <span class="host-name">Peter R. Vandamore, MBA, CASC, CPA.</span>
    Mr. Vandamore is the author of 10 books about the ASC industry and a frequent speaker at industry
  </div>
  <div class="available">Available On</div>
  <div class="platforms">
    <span>Soundvale</span><span>Brisk Shelf</span><span>ViewTrove</span><span>Wavelet</span><span>Castrill</span>
  </div>
  <div class="visit">Or Visit the Website At</div>
  <div class="site">www.clinicrulebookhour.example</div>
</section>

</body>
</html>
```